Pharmacy

Two sided postcard. Pictures on one side. Description on the other. We design and build pharmacies. pictures are some of our finished work. You can use as many pictures as you like not necessary to use all of them. Size of card should be 5"x7". See my website at display@brightfieldfixtures.com for more inspiration. I include the back of one card that I used recently. Both sids need design input. Feel free to contact me with questions.
Requirements
Must have
- Must be a two sided postcard
Nice to have
- I am sending a design of a sleek type postcard that I saw online as an example.
- https://lnk.example-pics.net/images/q7KmRz
- I am looking for something modern.
- Not limited to colors on my website.

```html
<!DOCTYPE html>
<html lang="en">
<head>
<meta charset="utf-8">
<title>Brightfield Showcase – Postcard Front and Back</title>
<link href="https://fonts.googleapis.com/css2?family=Arimo:wght@400;700&family=Roboto:wght@300;400;700&family=Varela+Round&family=Delius&display=swap" rel="stylesheet">
<style>
  :root {
    --maroon: #830000;
    --maroon-text: #8c1010;
    --gold: #c27a00;
    --icon-gold: #c98a1f;
    --pink: #c9868e;
    --grey-panel: #ececec;
    --grey-check: #f1f1f1;
    --ink: #333333;
    --body-grey: #555555;
    --card-border: #555555;
  }
  * { margin: 0; padding: 0; box-sizing: border-box; }
  html, body { width: 1200px; height: 1200px; overflow: hidden; background: #ffffff; }
  .canvas { position: relative; width: 1200px; height: 1200px; }
  .card {
    position: absolute; top: 208px; width: 700px; height: 980px;
    transform: scale(0.8); transform-origin: 0 0;
    background: #fdfdfd; overflow: hidden;
  }
  .card--front { left: 24px; border: 1px solid var(--card-border); }
  .card--back { left: 616px; border: 1px solid #bbbbbb; }
  .card svg.art { position: absolute; inset: 0; width: 700px; height: 980px; }

  .front-title {
    position: absolute; right: 51px; top: 100px;
    font-family: "Arimo", Arial, sans-serif; font-weight: 700;
    font-size: 29px; line-height: 36px; text-align: right;
    color: var(--maroon-text);
  }
  .contact { position: absolute; right: 52px; top: 756px; list-style: none; }
  .contact li {
    display: flex; align-items: center; justify-content: flex-end; gap: 12px;
    height: 27px; font-family: "Roboto", Arial, sans-serif; font-size: 16px; color: var(--ink);
  }
  .contact li.contact__name { font-weight: 700; }
  .contact li.contact__address { padding-right: 32px; }
  .contact svg { width: 20px; height: 20px; flex: none; }

  .back-title {
    position: absolute; left: 47px; top: 100px;
    font-family: "Arimo", Arial, sans-serif; font-weight: 700;
    font-size: 29px; line-height: 34px; color: #ffffff;
  }
  .values { position: absolute; left: 0; top: 248px; list-style: none; }
  .values li {
    width: 258px; height: 32px; margin-bottom: 12px; padding-left: 48px;
    background: var(--gold); color: #ffffff;
    font-family: "Varela Round", Arial, sans-serif; font-size: 28px; line-height: 32px;
    position: relative;
  }
  .values li::before { content: "•"; position: absolute; left: 48px; transform: translateX(-26px); }
  .about {
    position: absolute; left: 200px; width: 510px; top: 550px;
    font-family: "Delius", "Comic Sans MS", cursive; font-size: 22px; line-height: 36.3px;
    text-align: center; color: var(--body-grey); letter-spacing: 0.6px;
  }
  .indicia {
    position: absolute; left: 148px; width: 120px; top: 848px;
    font-family: "Roboto", Arial, sans-serif; font-weight: 700; font-size: 16px; line-height: 23px;
    text-align: center; color: var(--maroon);
  }
</style>
</head>
<body>
<div class="canvas">

  <section class="card card--front" aria-label="Postcard front">
    <svg class="art" viewBox="0 0 700 980" aria-hidden="false">
      <defs>
        <linearGradient id="pinkFade" x1="1" y1="0.5" x2="0" y2="0.5">
          <stop offset="0" stop-color="var(--pink)"/>
          <stop offset="1" stop-color="#ffffff"/>
        </linearGradient>
        <linearGradient id="storeWarm" x1="0" y1="0" x2="1" y2="1">
          <stop offset="0" stop-color="#c8a07a"/>
          <stop offset="0.5" stop-color="#8a6248"/>
          <stop offset="1" stop-color="#d8d2c8"/>
        </linearGradient>
        <linearGradient id="storeCool" x1="0" y1="0" x2="1" y2="1">
          <stop offset="0" stop-color="#d9d6cf"/>
          <stop offset="0.5" stop-color="#8fb3c4"/>
          <stop offset="1" stop-color="#5a4a40"/>
        </linearGradient>
      </defs>

      <g class="accent-diamonds">
        <rect x="-53" y="-53" width="106" height="106" rx="14" transform="translate(110 153) rotate(45)" fill="url(#pinkFade)"/>
        <rect x="-28" y="-28" width="57" height="57" rx="8" transform="translate(203 100) rotate(45)" fill="url(#pinkFade)"/>
        <rect x="-50" y="-50" width="99" height="99" rx="14" transform="translate(420 388) rotate(45)" fill="url(#pinkFade)"/>
        <rect x="-53" y="-53" width="106" height="106" rx="14" transform="translate(115 525) rotate(45)" fill="url(#pinkFade)"/>
        <rect x="-53" y="-53" width="106" height="106" rx="14" transform="translate(110 770) rotate(45)" fill="url(#pinkFade)"/>
      </g>

      <g class="project-photo" role="img" aria-label="Photo of a finished pharmacy interior with wood shelving and glass display counters">
        <rect x="-124" y="-124" width="247" height="247" rx="20" transform="translate(205 330) rotate(45)" fill="url(#storeWarm)"/>
      </g>
      <g class="project-photo" role="img" aria-label="Photo of pharmacy aisle with slatwall displays and orchid">
        <path d="M700 205 L435 400 L700 730 Z" fill="url(#storeCool)"/>
      </g>
      <g class="project-photo" role="img" aria-label="Photo of lit pharmacy shelving with personal care products">
        <rect x="-82" y="-82" width="163" height="163" rx="16" transform="translate(340 520) rotate(45)" fill="url(#storeCool)"/>
      </g>
      <g class="project-photo" role="img" aria-label="Photo of curved wood pharmacy gondola stocked with products">
        <rect x="-84" y="-84" width="167" height="167" rx="16" transform="translate(207 652) rotate(45)" fill="url(#storeWarm)"/>
      </g>
      <g class="project-photo" role="img" aria-label="Photo of pharmacy shelving detail">
        <rect x="-34" y="-34" width="68" height="68" rx="8" transform="translate(190 838) rotate(45)" fill="url(#storeWarm)"/>
      </g>
    </svg>

    <h1 class="front-title">BRIGHTFIELD SHOWCASE<br>&amp; STORE FURNITURE<br>CO INC.</h1>

    <ul class="contact">
      <li>201 555 0148
        <svg viewBox="0 0 20 20"><circle cx="10" cy="10" r="9" fill="var(--icon-gold)"/><path d="M7 5.5 L8.8 7.6 L7.8 8.8 Q9 11.4 11.2 12.2 L12.4 11.2 L14.5 13 L13.2 14.6 Q8.5 14.2 5.6 7 Z" fill="#fff"/></svg>
      </li>
      <li>display@brightfieldfixtures.com
        <svg viewBox="0 0 20 20"><circle cx="10" cy="10" r="9" fill="var(--icon-gold)"/><rect x="5" y="6.5" width="10" height="7" rx="1" fill="none" stroke="#fff" stroke-width="1.4"/><path d="M5.5 7 L10 10.5 L14.5 7" fill="none" stroke="#fff" stroke-width="1.4"/></svg>
      </li>
      <li>www.brightfieldfixtures.com
        <svg viewBox="0 0 20 20"><circle cx="10" cy="10" r="8.2" fill="none" stroke="var(--icon-gold)" stroke-width="1.6"/><ellipse cx="10" cy="10" rx="3.5" ry="8.2" fill="none" stroke="var(--icon-gold)" stroke-width="1.3"/><path d="M2 10 H18 M3.5 6 H16.5 M3.5 14 H16.5" stroke="var(--icon-gold)" stroke-width="1.3"/></svg>
      </li>
      <li class="contact__name">Brightfield Showcase &amp; Store Fixture Co. inc.
        <svg viewBox="0 0 20 20"><circle cx="10" cy="10" r="9" fill="var(--icon-gold)"/><path d="M10 15.5 Q6 11 6 8.5 A4 4 0 0 1 14 8.5 Q14 11 10 15.5 Z" fill="#fff"/><circle cx="10" cy="8.5" r="1.6" fill="var(--icon-gold)"/></svg>
      </li>
      <li class="contact__address">PO Box 318, Fairview NJ 07022</li>
    </ul>
  </section>

  <section class="card card--back" aria-label="Postcard back">
    <svg class="art" viewBox="0 0 700 980">
      <rect class="checker-area" x="395" y="0" width="300" height="140" fill="var(--grey-check)" role="img" aria-label="Light checker pattern area"/>
      <path class="checker-area" d="M50 980 L200 830 L360 980 Z" fill="var(--grey-check)" role="img" aria-label="Light checker pattern area"/>
      <rect class="panel" x="-205" y="-205" width="410" height="410" rx="50" transform="translate(430 630) rotate(45)" fill="var(--grey-panel)"/>
      <path class="maroon-block" d="M0 0 H350 L530 180 Q548 212 530 238 L40 728 Q26 740 0 740 Z" fill="var(--maroon)"/>
      <line x1="0" y1="380" x2="198" y2="572" stroke="#ffffff" stroke-width="3"/>
      <path d="M520 2 L425 97 Q410 118 428 140 L700 420" fill="none" stroke="#8a8a8a" stroke-width="3"/>
      <rect x="-50" y="-50" width="100" height="100" rx="18" transform="translate(585 318) rotate(45)" fill="none" stroke="#222" stroke-width="4"/>
      <rect x="-55" y="-55" width="110" height="110" rx="18" transform="translate(690 388) rotate(45)" fill="url(#backPink)"/>
      <defs>
        <linearGradient id="backPink" x1="1" y1="0.5" x2="0" y2="0.5">
          <stop offset="0" stop-color="var(--pink)"/>
          <stop offset="1" stop-color="#ffffff"/>
        </linearGradient>
      </defs>
      <path class="stripe-area" d="M700 50 L700 270 L565 135 L655 45 Z" fill="#9a9a9a" role="img" aria-label="Diagonal stripe pattern"/>
      <path class="stripe-area" d="M40 770 L110 715 L185 790 L115 858 Z" fill="#9a9a9a" role="img" aria-label="Diagonal stripe pattern"/>
      <path d="M612 980 L660 920 Q680 895 700 905" fill="none" stroke="#222" stroke-width="4"/>
      <path d="M700 862 L690 872 L700 882 Z" fill="var(--maroon)"/>
    </svg>

    <h2 class="back-title">BRIGHTFIELD SHOWCASE<br>&amp; STORE FURNITURE<br>CO INC.</h2>

    <ul class="values">
      <li>Quality</li>
      <li>Experience</li>
      <li>Innovation</li>
    </ul>

    <p class="about">Family owned and operated for<br>three generations Brightfield Showcase &amp;<br>Store Fixture Co. Inc is the oldest store<br>fixture company in New Jersey.<br>As Designers &amp; Manufacturers we can save<br>you hours of time and money. Our level of<br>experience will be evident from the<br>outset and you will be pleased<br>that you found us.</p>

    <p class="indicia">Presorted<br>First Class<br>US Postage<br>Paid<br>Mailpath</p>
  </section>

</div>
</body>
</html>
```